KeyHarbor needs a modern business card

We are a modern conveyancing company and we need to appeal to the top (Multi-million dollar properties)and bottom on the property conveyancing market but our sweet spot is the middle of the market. I like professional with a hint of unconventional.

Target Market(s)

As above

Industry/Entity Type

Real Estate

Contact Information for Business Card

Back Of card:
thinking black with the logo and a tag line (I could be wrong about the black)
Tag line - Clear Advice, Calm Settlements

Front of Card:
Marissa Toll (BBus (Finance) LLB)
Licensed Conveyancer
Email: marissa@keyharbor.com.au

Key Harbor
ABN: 48 913 706
Suite 14, Level 3, 9 Calloway Road Lindhurst Park, NSW 2178
Phone: 1300 682 917

Sydney - Melbourne - Brisbane (Perhaps have this along the bottom of the card)

Requirements
Must have
• Sleek, modern and top end appeal (But approachable)
Should not have
• Not too cluttered

```html
<!DOCTYPE html>
<html lang="en">
<head>
<meta charset="utf-8">
<title>KeyHarbor Business Card</title>
<link rel="stylesheet" href="https://fonts.googleapis.com/css2?family=Exo+2:wght@300;400;500;600&display=swap">
<style>
  :root {
    --page: #e9e7e3;
    --card-dark: #050607;
    --card-light: #ffffff;
    --brand-grey: #4a4a4c;
    --accent-blue: #2d5c86;
    --accent-green: #4aa532;
    --text-grey: #555759;
    --rule: #1e3a5a;
    --white: #ffffff;
    --badge: #2b2b2d;
  }
  * { box-sizing: border-box; margin: 0; padding: 0; }
  html, body {
    width: 1200px; height: 789px; overflow: hidden;
    background: var(--page);
    font-family: "Exo 2", sans-serif;
  }
  .canvas {
    width: 1200px; height: 789px;
    display: flex; align-items: center; justify-content: center; gap: 40px;
  }
  .card {
    position: relative;
    width: 540px; height: 309px;
    border-radius: 3px;
    overflow: hidden;
    box-shadow: 0 6px 18px rgba(0,0,0,.18);
  }

  /* Back of card */
  .card--back { background: var(--card-dark); }
  .back-tiles {
    position: absolute; inset: 0;
    background:
      linear-gradient(135deg, transparent 55%, rgba(95,143,52,.75) 80%, rgba(60,100,40,.5) 100%),
      linear-gradient(225deg, transparent 60%, rgba(46,92,102,.7) 100%),
      linear-gradient(45deg, rgba(46,92,102,.55) 0%, transparent 35%),
      linear-gradient(160deg, rgba(31,58,85,.85) 0%, transparent 40%),
      linear-gradient(200deg, rgba(31,58,85,.8) 0%, transparent 45%),
      var(--card-dark);
  }
  .back-brand {
    position: absolute; left: 0; right: 0; top: 180px;
    text-align: center; color: var(--white);
  }
  .back-brand__name {
    font-size: 46px; font-weight: 500; letter-spacing: .5px; line-height: 1;
  }
  .back-brand__tagline {
    margin-top: 10px; font-size: 15px; font-weight: 400; letter-spacing: .6px;
  }

  /* Front of card */
  .card--front { background: var(--card-light); }
  .front-brand {
    position: absolute; right: 26px; top: 22px; text-align: right;
  }
  .front-brand__name {
    font-size: 50px; font-weight: 500; color: var(--brand-grey); line-height: 1;
  }
  .front-brand__abn {
    margin-top: 4px; font-size: 12px; color: var(--accent-blue); letter-spacing: .3px;
  }
  .rule {
    position: absolute; height: 1px; background: var(--rule);
  }
  .rule--top { left: 250px; right: 26px; top: 100px; }
  .rule--mid { left: 240px; right: 26px; top: 188px; }
  .rule--bottom { left: 30px; right: 26px; top: 294px; }

  .person {
    position: absolute; right: 26px; top: 118px; text-align: right;
  }
  .person__name {
    font-size: 24px; font-weight: 500; color: var(--accent-green); line-height: 1.05;
    padding-right: 34px;
  }
  .person__badge {
    position: absolute; right: 0; top: 2px;
    width: 24px; height: 24px; border-radius: 50%; background: var(--badge);
  }
  .person__role, .person__quals {
    font-size: 12.5px; color: var(--text-grey); line-height: 1.25; padding-right: 34px;
  }

  .contact {
    position: absolute; left: 30px; top: 200px;
    list-style: none;
  }
  .contact__item {
    display: flex; align-items: center; gap: 10px;
    font-size: 14px; color: var(--text-grey); height: 22px;
  }
  .contact__icon { width: 16px; height: 16px; flex: none; }
  .address {
    position: absolute; left: 0; right: 26px; top: 252px;
    text-align: right; font-size: 13px; font-weight: 500; color: var(--text-grey); line-height: 1.3;
  }
</style>
</head>
<body>
<main class="canvas">

  <section class="card card--back" aria-label="Back of card">
    <div class="back-tiles" role="img" aria-label="Overlapping translucent navy, teal and green geometric tiles on black"></div>
    <div class="back-brand">
      <div class="back-brand__name">KeyHarbor</div>
      <div class="back-brand__tagline">Clear Advice, Calm Settlements</div>
    </div>
  </section>

  <section class="card card--front" aria-label="Front of card">
    <div class="front-brand">
      <div class="front-brand__name">KeyHarbor</div>
      <div class="front-brand__abn">ABN: 48 913 706</div>
    </div>
    <div class="rule rule--top"></div>

    <div class="person">
      <span class="person__badge"></span>
      <div class="person__name">Marissa Toll</div>
      <div class="person__role">Licensed Conveyancer</div>
      <div class="person__quals">BBus (Finance) LLB</div>
    </div>
    <div class="rule rule--mid"></div>

    <ul class="contact">
      <li class="contact__item">
        <svg class="contact__icon" viewBox="0 0 16 16" aria-hidden="true">
          <circle cx="8" cy="8" r="8" fill="#4aa532"/>
          <path d="M5.2 4.2l1.4-.3.8 1.8-.9.7c.4 1 1.2 1.8 2.1 2.2l.7-.9 1.8.8-.3 1.4c-3 .2-5.9-2.7-5.6-5.7z" fill="#fff"/>
        </svg>
        1300 682 917
      </li>
      <li class="contact__item">
        <svg class="contact__icon" viewBox="0 0 16 16" aria-hidden="true">
          <rect x="1" y="3.5" width="14" height="9" rx="1" fill="#4aa532"/>
          <path d="M1.5 4l6.5 5 6.5-5" fill="none" stroke="#fff" stroke-width="1.2"/>
        </svg>
        marissa@keyharbor.com.au
      </li>
    </ul>

    <div class="address">Suite 14, Level 3, 9 Calloway Road Lindhurst Park,<br>NSW 2178</div>
    <div class="rule rule--bottom"></div>
  </section>

</main>
</body>
</html>
```